New business card with our logo

we finalized our logo with the help of pixel harbor - now we need a business card using that logo. we are a metal service center providing raw steel and metal products for fabricating, contractors, artists, etc. we have the wording for the back of the card figured out (attached, no deviations from text please), just need help putting it all together.
Contact Information for Business Card
would like the look of steel somehow incorporated in the design ... would like the black part of the logo to be steel or silver color (the S & MORROW)
Font styles to use
Other font styles liked:
- calibri, arial, similar to those, modern looking
Colors
Designer to choose colors to be used in the design.
Requirements
Must have
- Back of card must haves are attached (no deviations from wording please).
- FRONT of card:
- logo
- address
- name
- office tel
- cell
- fax
- website
- address
Nice to have
- incorporate the look of steel or element of steel somehow
- names of the staff on front not in all caps, i.e. Tereza not TEREZA
- this industry is more industrial, not coffee or flower shop so design should be aligned with that
- design should be classic and tasteful

```html
<!DOCTYPE html>
<html lang="en">
<head>
<meta charset="utf-8">
<title>Morrow Steel – Business Card Design</title>
<link rel="stylesheet" href="https://fonts.googleapis.com/css2?family=Lato:ital,wght@0,300;0,400;0,700;0,900;1,400&display=swap">
<style>
  :root {
    --stage-dark: #23272c;
    --stage-mid: #4a535c;
    --card-black: #17181b;
    --card-edge: #0d0e10;
    --steel-blue: #1c74c6;
    --silver: #d5d8dc;
    --silver-dim: #a9aeb4;
    --text-light: #e9ebee;
    --caption-band: #b3b3b3;
    --caption-ink: #151515;
  }
  * { box-sizing: border-box; margin: 0; padding: 0; }
  html, body { width: 1200px; height: 1200px; overflow: hidden; }
  body {
    font-family: "Lato", Arial, sans-serif;
    background: var(--caption-band);
    color: var(--text-light);
  }
  .stage {
    position: relative;
    width: 1200px;
    height: 892px;
    background: radial-gradient(ellipse at 35% 40%, var(--stage-mid) 0%, var(--stage-dark) 75%);
  }

  /* Brand mark presentation */
  .brand-showcase {
    position: absolute;
    left: 60px;
    top: 300px;
    width: 420px;
    display: flex;
    flex-direction: column;
    align-items: center;
    gap: 26px;
  }
  .brand-dot {
    width: 120px;
    height: 120px;
    border-radius: 50%;
    border: 8px solid var(--steel-blue);
  }
  .brand-showcase .brand-name {
    font-size: 46px;
    font-weight: 900;
    letter-spacing: 1px;
    color: var(--silver);
  }

  /* Cards */
  .card {
    position: absolute;
    width: 620px;
    height: 354px;
    background: var(--card-black);
    border-radius: 22px;
    box-shadow: 0 6px 0 var(--card-edge), 0 12px 0 var(--card-edge), 0 24px 40px rgba(0,0,0,.55);
    overflow: hidden;
  }
  .card-front { left: 530px; top: 40px; }
  .card-back  { left: 530px; top: 460px; }

  .card-brand {
    display: flex;
    align-items: center;
    gap: 12px;
  }
  .brand-dot-small {
    width: 38px; height: 38px;
    border-radius: 50%;
    border: 4px solid var(--steel-blue);
  }
  .card-brand .brand-name {
    font-weight: 900;
    color: var(--silver);
    letter-spacing: .5px;
    white-space: nowrap;
  }

  /* Front side */
  .card-front .card-brand { position: absolute; left: 34px; top: 30px; }
  .card-front .card-brand .brand-name { font-size: 30px; }
  .holder {
    position: absolute;
    top: 112px; left: 0; right: 0;
    text-align: center;
  }
  .holder-name { font-size: 25px; font-weight: 400; color: var(--text-light); }
  .holder-title {
    display: inline-block;
    margin-top: 2px;
    font-size: 14px;
    font-weight: 300;
    color: var(--silver-dim);
    padding-bottom: 4px;
    border-bottom: 3px solid var(--steel-blue);
  }
  .contact-line {
    position: absolute;
    left: 100px; right: 100px; top: 223px;
    height: 1px;
    background: var(--steel-blue);
    opacity: .7;
  }
  .contact-row {
    position: absolute;
    left: 30px; right: 30px; top: 204px;
    display: flex;
    justify-content: space-between;
  }
  .contact-item {
    width: 180px;
    display: flex;
    flex-direction: column;
    align-items: center;
    gap: 12px;
    font-size: 12.5px;
    line-height: 1.45;
    color: var(--text-light);
    text-align: center;
  }
  .contact-icon {
    width: 38px; height: 38px;
    border-radius: 50%;
    background: var(--steel-blue);
    display: flex; align-items: center; justify-content: center;
  }
  .contact-icon svg { width: 20px; height: 20px; }

  /* Back side */
  .card-back .card-brand {
    position: absolute;
    left: 36px; top: 40px;
    width: 260px;
    flex-direction: column;
    gap: 14px;
  }
  .card-back .brand-dot-back {
    width: 104px; height: 104px;
    border-radius: 50%;
    border: 7px solid var(--steel-blue);
  }
  .card-back .card-brand .brand-name { font-size: 32px; }
  .rule {
    position: absolute;
    height: 1px;
    background: var(--silver-dim);
  }
  .rule-left { left: 0; width: 30px; top: 92px; }
  .rule-right { left: 320px; right: 0; top: 140px; }
  .rule-under { left: 320px; right: 0; top: 212px; }
  .service-head {
    position: absolute;
    left: 330px; top: 150px;
    font-size: 19px;
    font-weight: 900;
    color: var(--text-light);
    letter-spacing: .5px;
    white-space: nowrap;
  }
  .service-ops {
    position: absolute;
    left: 330px; top: 180px;
    font-size: 14px;
    color: var(--text-light);
    white-space: nowrap;
  }
  .service-ops .sep { color: var(--steel-blue); margin: 0 4px; }
  .product-list {
    position: absolute;
    left: 0; right: 0; top: 244px;
    text-align: center;
    font-size: 12.5px;
    color: var(--text-light);
  }
  .product-list .sep { color: var(--steel-blue); margin: 0 5px; }
  .tagline {
    position: absolute;
    left: 0; right: 0; top: 276px;
    text-align: center;
    font-size: 14px;
    font-style: italic;
    color: var(--text-light);
  }

  .caption {
    height: 308px;
    display: flex;
    align-items: center;
    justify-content: center;
    font-size: 58px;
    font-weight: 400;
    color: var(--caption-ink);
  }
</style>
</head>
<body>
  <section class="stage">
    <div class="brand-showcase">
      <div class="brand-dot"></div>
      <div class="brand-name">MORROW STEEL</div>
    </div>

    <article class="card card-front">
      <div class="card-brand">
        <div class="brand-dot-small"></div>
        <div class="brand-name">MORROW STEEL</div>
      </div>
      <div class="holder">
        <div class="holder-name">Daniel Brennan</div>
        <div class="holder-title">Director</div>
      </div>
      <div class="contact-line"></div>
      <div class="contact-row">
        <div class="contact-item">
          <div class="contact-icon">
            <svg viewBox="0 0 24 24" fill="#fff"><path d="M6.6 10.8a15.1 15.1 0 0 0 6.6 6.6l2.2-2.2c.3-.3.7-.4 1-.2 1.1.4 2.3.6 3.6.6.6 0 1 .4 1 1V20c0 .6-.4 1-1 1C10.6 21 3 13.4 3 4c0-.6.4-1 1-1h3.5c.6 0 1 .4 1 1 0 1.3.2 2.5.6 3.6.1.3 0 .7-.2 1z"/></svg>
          </div>
          <div>(office) - 123 456 7890<br>(mobile) - 001 235 4589<br>(fax) - 123 456 7898</div>
        </div>
        <div class="contact-item">
          <div class="contact-icon">
            <svg viewBox="0 0 24 24" fill="none" stroke="#fff" stroke-width="1.8"><circle cx="12" cy="12" r="9"/><path d="M3 12h18M12 3c3 3 3 15 0 18M12 3c-3 3-3 15 0 18"/></svg>
          </div>
          <div>yourwebsitename.com<br>yourname@email.com</div>
        </div>
        <div class="contact-item">
          <div class="contact-icon">
            <svg viewBox="0 0 24 24" fill="#fff"><path d="M12 2a7 7 0 0 0-7 7c0 5 7 13 7 13s7-8 7-13a7 7 0 0 0-7-7zm0 9.5A2.5 2.5 0 1 1 12 6.5a2.5 2.5 0 0 1 0 5z"/></svg>
          </div>
          <div>Street adress, loremp ipsum<br>Your city, 1568</div>
        </div>
      </div>
    </article>

    <article class="card card-back">
      <div class="rule rule-left"></div>
      <div class="card-brand">
        <div class="brand-dot-back"></div>
        <div class="brand-name">MORROW STEEL</div>
      </div>
      <div class="rule rule-right"></div>
      <div class="service-head">METAL SERVICES CENTER</div>
      <div class="service-ops">CUT<span class="sep">•</span>SHEAR<span class="sep">•</span>PUNCH<span class="sep">•</span>LIGHT FAB</div>
      <div class="rule rule-under"></div>
      <div class="product-list">Structural Steel<span class="sep">|</span>Stainless &amp; Aluminum<span class="sep">|</span>Building Components<span class="sep">|</span>Rebar<span class="sep">|</span>Decking<span class="sep">|</span>... And more!</div>
      <div class="tagline">Cut to size, Pick-up or Delivered!</div>
    </article>
  </section>

  <footer class="caption">Business Card Design, front &amp; Back</footer>
</body>
</html>
```